Progressive European Honey Business needs minimalistic packaging design

Hello - thank you for your interest in our brief. We are Velvet Jinx, a London based Honey business, importing only the best honey Europe has to offer. Our values are deeply rooted with in progressive liberal values and we are looking for minimalist packaging, which reflects that.

We are looking for a design, which dimensions fit with our packaging option (Kelmor Glass Jar | HEIGHT 90mm | DIAMETER 63mm). We will require a various output files (High Resolution JPEG (CMYK Colors 300 dpi) Source File Ai, PSD, PDF, Printing files (die cut, die folding) and a 3D Mockup of the packaging for use within digital commerce platforms.

We must be able to adjust the free text on the label front and it should include the following:
Brand Name
Honey type
Limited edition No. X / 100 ( X being the number of purchase i.e. 25 / 100)
EU Honey, Single Orgin (Germany)
(c) The net weight (250g)

The back must include room for additional information (again adjustable by us) and the following:
“Unsuitable for children under 12 months”
(b) The appropriate durability declaration

In total, we are looking for
a) A front label
b) A back label
c) A seal (round) including the attached bee and logo included in the Zip file.
Do note that a) & b) can also be combined into one design as long as the symmetry on the jar stays intact.

The final design should communicate modern aesthetics, high quality, that are slightly provocative and pop off the shelves.
Updates

Hi folks, sorry for the delay in completing this project, but my business partner had a leak in his house. We planned to finalise our review today, but this will have to wait until it's no longer raining in his livingroom. Our sincere apologies!

Other font styles liked:
• See branding guidelines

Requirements
Must have
• Must follow the branding guideline and fonts provided as attachment

```html
<!DOCTYPE html>
<html lang="en">
<head>
<meta charset="utf-8">
<title>Velvet Jinx – Flower Honey Label Set</title>
<link rel="stylesheet" href="https://fonts.googleapis.com/css2?family=Rammetto+One&family=Roboto:wght@400;500;700&family=Roboto+Mono:wght@500&display=swap">
<style>
  :root {
    --purple: #7b2a7b;
    --purple-deep: #6e2470;
    --orange: #f26a2e;
    --panel-grey: #d6dedd;
    --ink: #2a2a2a;
    --rule: #6b6b6b;
    --soft-lilac: #d9bde0;
    --page: #ffffff;
    --bee-yellow: #f3c532;
    --bee-black: #1d1d1d;
  }
  * { box-sizing: border-box; margin: 0; padding: 0; }
  html, body { width: 1200px; height: 902px; overflow: hidden; background: var(--page); }
  .canvas { position: relative; width: 1200px; height: 902px; }

  /* Round seal */
  .seal {
    position: absolute; left: 350px; top: 22px; width: 270px; height: 270px;
    border-radius: 50%; background: var(--purple);
    display: flex; flex-direction: column; align-items: center; justify-content: center;
    font-family: "Rammetto One", "Roboto", sans-serif; color: var(--orange);
    font-size: 36px; line-height: 54px; text-align: center;
  }

  /* Tamper strip */
  .seal-strip {
    position: absolute; left: 468px; top: 288px; width: 30px; height: 179px;
    background: var(--orange);
  }
  .seal-strip__text {
    position: absolute; left: 50%; top: 55%;
    transform: translate(-50%, -50%) rotate(-90deg);
    white-space: nowrap; font-family: "Roboto", sans-serif; font-weight: 500;
    font-size: 12px; letter-spacing: 0.2px; color: var(--purple);
  }

  /* Wrap-around label */
  .label {
    position: absolute; left: 41px; top: 467px; width: 653px; height: 330px;
    display: flex; background: var(--purple);
  }
  .label__margin { width: 22px; background: var(--purple); }

  .label-back {
    width: 215px; background: var(--panel-grey);
    padding: 40px 22px 0 31px;
    font-family: "Roboto", sans-serif; color: var(--ink);
  }
  .label-back__brand {
    font-family: "Rammetto One", sans-serif; color: var(--purple);
    font-size: 15px; line-height: 1; font-weight: 400;
    padding-bottom: 6px; border-bottom: 2px solid var(--orange); margin-bottom: 12px;
  }
  .label-back__copy {
    font-size: 8.6px; line-height: 10.7px; text-transform: uppercase; text-align: justify;
    padding-bottom: 5px; border-bottom: 1px solid var(--rule);
  }
  .label-back__row {
    font-size: 8.6px; line-height: 11px; text-transform: uppercase;
    padding: 8px 0 5px; border-bottom: 1px solid var(--rule);
  }
  .label-back__date {
    display: block; font-family: "Roboto Mono", monospace; font-size: 12px; letter-spacing: 1.5px; margin-top: 2px;
  }
  .label-back__row--last { border-bottom: 2px solid var(--orange); padding-bottom: 5px; }
  .label-back__social {
    font-size: 10px; font-weight: 700; color: var(--purple); margin-top: 9px;
  }

  .label-front { position: relative; flex: 1; background: var(--purple-deep); }
  .label-front__variety {
    position: absolute; left: 46px; top: 30px;
    font-family: "Roboto", sans-serif; font-weight: 700; color: var(--orange);
    font-size: 72px; line-height: 68px; letter-spacing: 0;
  }
  .label-front__mascot {
    position: absolute; left: 226px; top: 38px; width: 152px; height: 220px;
    border-radius: 42% 42% 36% 36%;
    background: linear-gradient(160deg, var(--bee-yellow) 0%, var(--bee-yellow) 40%, var(--bee-black) 75%);
  }
  .label-front__meta {
    position: absolute; left: 230px; top: 272px;
    font-family: "Roboto", sans-serif; font-size: 12px; color: var(--soft-lilac); white-space: nowrap;
  }
  .label-front__divider { color: var(--orange); margin: 0 3px; }
</style>
</head>
<body>
<main class="canvas">
  <div class="seal"><span>VELVET</span><span>JINX</span></div>

  <div class="seal-strip"><span class="seal-strip__text">LIMITED EDITION</span></div>

  <section class="label">
    <div class="label__margin"></div>

    <div class="label-back">
      <h2 class="label-back__brand">VELVET JINX</h2>
      <p class="label-back__copy">Lorem ipsum dolor sit amet, consectetuer adipiscing elit, sed estad diam nonummy nibh euismod tincidunt ut laoreet dolore magna aliquam erat volutpat diam nonummy vers.</p>
      <p class="label-back__row">Single origin: Germany</p>
      <p class="label-back__row">Storage: dry, cool, dark</p>
      <p class="label-back__row">Unsuitable for children<br>under 12 months</p>
      <p class="label-back__row label-back__row--last">Best used before:<span class="label-back__date">XX.XX.XXXX</span></p>
      <p class="label-back__social">picturely @ velvetjinx_uk</p>
    </div>

    <div class="label-front">
      <h1 class="label-front__variety">FLO<br>WER<br>HON<br>NEY</h1>
      <div class="label-front__mascot" role="img" aria-label="Brand mascot: a crowned cartoon bee holding a honey drop"></div>
      <p class="label-front__meta">GERMAN PRODUCT<span class="label-front__divider">|</span>250g</p>
    </div>
  </section>
</main>
</body>
</html>
```